Lavoie Roofing

Want a professional looking business card

Industry/Entity Type

Business

Contact Information for Business Card

Mark Lavoie ( Owner) mark@lavoieroofing.example, www.lavoieroofing.example, Adress: 4712 County road 31 Brookhaven,ON X0A2M4

```html
<!DOCTYPE html>
<html lang="en">
<head>
<meta charset="utf-8">
<title>Lavoie Roofing — Business Card</title>
<link rel="stylesheet" href="https://fonts.googleapis.com/css2?family=Open+Sans:wght@400;600;700&display=swap">
<style>
  :root {
    --brand-blue: #1b4585;
    --brand-blue-soft: #24508f;
    --paper: #ffffff;
    --ink-grey: #555b63;
    --rule-grey: #c9ccd1;
    --edge-tint: #b9c3d3;
    --backdrop: #e7e5e2;
  }
  * { box-sizing: border-box; margin: 0; padding: 0; }
  html, body { width: 1200px; height: 997px; overflow: hidden; }
  body {
    background: var(--backdrop);
    font-family: "Open Sans", Arial, sans-serif;
    position: relative;
  }
  .card {
    position: absolute;
    left: 250px;
    width: 700px;
    height: 400px;
    overflow: hidden;
    box-shadow: 0 6px 18px rgba(0,0,0,0.12);
  }

  /* Front */
  .card-front { top: 62px; background: var(--brand-blue); }
  .front-map {
    position: absolute;
    left: 90px; top: 40px; width: 520px; height: 250px;
    background: radial-gradient(ellipse at center, var(--brand-blue-soft) 0%, var(--brand-blue) 70%);
  }
  .front-name {
    position: absolute;
    left: 0; right: 0; top: 150px;
    text-align: center;
    color: var(--paper);
    font-weight: 700;
    font-size: 46px;
    letter-spacing: 3px;
    text-transform: uppercase;
  }
  .front-band { position: absolute; left: 0; bottom: 0; width: 700px; height: 80px; }
  .front-url {
    position: absolute;
    right: 110px; bottom: 22px;
    color: var(--brand-blue);
    font-size: 15px;
  }

  /* Back */
  .card-back { top: 522px; background: var(--paper); }
  .back-name {
    position: absolute;
    left: 40px; top: 118px;
    color: var(--brand-blue);
    font-weight: 700;
    font-size: 36px;
    letter-spacing: 2px;
    text-transform: uppercase;
  }
  .back-rule {
    position: absolute;
    left: 40px; top: 258px; width: 330px; height: 1px;
    background: var(--rule-grey);
  }
  .contact-list { position: absolute; left: 40px; top: 276px; list-style: none; }
  .contact-list li {
    display: flex; align-items: center; gap: 8px;
    color: var(--ink-grey); font-size: 15px; line-height: 24px;
  }
  .contact-icon { width: 17px; height: 17px; flex: none; }
  .person { position: absolute; right: 40px; top: 58px; text-align: right; }
  .person-name { color: var(--brand-blue); font-weight: 700; font-size: 18px; }
  .person-role {
    color: #8a8f96; font-size: 14px;
    border-bottom: 1px solid var(--rule-grey);
    padding: 0 0 2px 60px; display: inline-block;
  }
  .address {
    position: absolute; right: 40px; top: 140px;
    text-align: right; font-size: 15px; line-height: 21px; color: var(--ink-grey);
  }
  .address-company { color: var(--brand-blue); }
  .back-band { position: absolute; left: 0; bottom: 0; width: 700px; height: 150px; }
</style>
</head>
<body>
  <section class="card card-front">
    <div class="front-map" role="img" aria-label="Faint dotted world map in the background"></div>
    <div class="front-name">Lavoie Roofing</div>
    <svg class="front-band" viewBox="0 0 700 80" aria-hidden="true">
      <polygon points="300,80 330,42 640,32 700,18 700,80" fill="#ffffff"/>
      <polygon points="640,32 700,18 700,10 652,22" fill="#b9c3d3"/>
    </svg>
    <div class="front-url">www.lavoieroofing.example</div>
  </section>

  <section class="card card-back">
    <div class="back-name">Lavoie Roofing</div>
    <div class="back-rule"></div>
    <ul class="contact-list">
      <li>
        <svg class="contact-icon" viewBox="0 0 17 17" aria-hidden="true"><rect width="17" height="17" fill="#1b4585"/><path d="M5 4l2 0 1 3-1.2 1a6 6 0 0 0 2.2 2.2L10 9l3 1v2a1 1 0 0 1-1 1A8 8 0 0 1 4 5a1 1 0 0 1 1-1z" fill="#fff"/></svg>
        (555) 010-0142
      </li>
      <li>
        <svg class="contact-icon" viewBox="0 0 17 17" aria-hidden="true"><rect width="17" height="17" fill="#1b4585"/><rect x="3.5" y="5" width="10" height="7" fill="none" stroke="#fff" stroke-width="1.2"/><path d="M3.5 5l5 4 5-4" fill="none" stroke="#fff" stroke-width="1.2"/></svg>
        mark@lavoieroofing.example
      </li>
      <li>
        <svg class="contact-icon" viewBox="0 0 17 17" aria-hidden="true"><rect width="17" height="17" fill="#1b4585"/><circle cx="8.5" cy="8.5" r="4.8" fill="none" stroke="#fff" stroke-width="1.1"/><ellipse cx="8.5" cy="8.5" rx="2" ry="4.8" fill="none" stroke="#fff" stroke-width="1"/><path d="M3.7 8.5h9.6" stroke="#fff" stroke-width="1"/></svg>
        www.lavoieroofing.example
      </li>
    </ul>
    <div class="person">
      <div class="person-name">MARK LAVOIE</div>
      <div class="person-role">Owner</div>
    </div>
    <div class="address">
      <div class="address-company">Lavoie Roofing</div>
      <div>4712 County road 31,</div>
      <div>Brookhaven,ON X0A2M4</div>
    </div>
    <svg class="back-band" viewBox="0 0 700 150" aria-hidden="true">
      <polygon points="318,150 330,112 580,26 640,26 700,40 700,150" fill="#1b4585"/>
      <polygon points="306,150 318,112 330,112 318,150" fill="#b9c3d3"/>
    </svg>
  </section>
</body>
</html>
```